Business Card and Letterhead for Vantage Psychology

We need a business card design and letterhead to use for our Psychology firm that specializes in psychoeducational assessments and individual therapy. Our motto is Purpose-Driven Assessments, Meaning-Centered Therapy.Our contact information is as follows:
Vantage Psychology
The Marwick Block - 6127-48St.
Box 2716 Olds, AB
T2K 3M8
t 403.555.0148 (VANT)
f 403.555.0172
www.vantagepsychology-example.ca
The business card will be used for two different psychologists so I can supply names nearer to completion. We prefer clean, uncluttered looks.

Target Market(s)

Clients, Educators

Font styles to use
Sans Serif

Colors

Designer to choose colors to be used in the design.

Requirements
Must have
• All relevant contact info, logo, some "white" space.
Nice to have
• It would be nice to see letterhead options that have the logo on the top of the page but also options that have it on the side. I think top of the page is probably our preference.
Should not have
• Too much clutter!

```html
<!DOCTYPE html>
<html lang="en">
<head>
<meta charset="utf-8">
<title>Vantage Psychology – Stationery</title>
<link href="https://fonts.googleapis.com/css2?family=Lato:wght@400;700&display=swap" rel="stylesheet">
<style>
  :root {
    --backdrop: #e4e4e4;
    --paper: #ffffff;
    --brand-blue: #55bcdb;
    --brand-orange: #f5a640;
  }
  * { margin: 0; padding: 0; box-sizing: border-box; }
  html, body {
    width: 1200px; height: 1200px; overflow: hidden;
    background: var(--backdrop);
    font-family: "Lato", sans-serif;
  }
  .stage { position: relative; width: 1200px; height: 1200px; }
  .sheet { position: absolute; background: var(--paper); }

  /* Letterhead */
  .letterhead { left: 435px; top: 123px; width: 675px; height: 954px; }
  .brand-mark { position: absolute; left: 50%; transform: translateX(-50%); border-radius: 50%; background: var(--brand-blue); }
  .brand-name {
    position: absolute; left: 0; right: 0; text-align: center;
    color: var(--brand-blue); font-weight: 700; letter-spacing: 0.06em;
    text-transform: uppercase; white-space: nowrap;
  }
  .letterhead .brand-mark { top: 58px; width: 80px; height: 80px; }
  .letterhead .brand-name { top: 140px; font-size: 21px; }
  .letterhead-footer { position: absolute; left: 0; right: 0; top: 833px; }
  .footer-item {
    position: absolute; top: 0; width: 190px; margin-left: -95px;
    text-align: center; color: var(--brand-blue); font-size: 11px; line-height: 15px;
    white-space: nowrap;
  }
  .footer-item svg { display: block; margin: 0 auto 25px; width: 32px; height: 32px; }
  .footer-phone { left: 170px; }
  .footer-address { left: 344px; }
  .footer-web { left: 530px; width: 220px; margin-left: -110px; }

  /* Card front */
  .card-front { left: 90px; top: 399px; width: 296px; height: 169px; }
  .card-front .brand-mark { top: 55px; width: 58px; height: 58px; }
  .card-front .brand-name { top: 116px; font-size: 14px; }

  /* Card back */
  .card-back { left: 91px; top: 632px; width: 295px; height: 169px; overflow: hidden; }
  .card-back-panel { position: absolute; left: 0; top: 0; width: 130px; height: 169px; background: var(--brand-blue); }
  .card-back-info { position: absolute; left: 130px; top: 0; right: 0; bottom: 0; }
  .card-back .brand-mark { left: 77px; top: 13px; width: 24px; height: 24px; transform: none; }
  .card-back .brand-name { left: 16px; right: auto; top: 41px; font-size: 7.5px; text-align: left; letter-spacing: 0.04em; }
  .contact-list { position: absolute; left: 23px; top: 66px; list-style: none; }
  .contact-row { position: relative; padding-left: 22px; font-size: 6px; line-height: 8px; color: var(--brand-blue); height: 16px; white-space: nowrap; }
  .contact-row.is-orange { color: var(--brand-orange); }
  .contact-row.is-tall { height: 26px; }
  .contact-row svg { position: absolute; left: 0; top: -1px; width: 13px; height: 13px; }
</style>
</head>
<body>
<main class="stage">

  <section class="sheet letterhead" aria-label="Letterhead">
    <div class="brand-mark"></div>
    <div class="brand-name">Vantage Psychology</div>

    <footer class="letterhead-footer">
      <div class="footer-item footer-phone">
        <svg viewBox="0 0 32 32" fill="none" stroke="var(--brand-blue)" stroke-width="1.2">
          <rect x="2" y="2" width="28" height="28"/>
          <path d="M6 8c2-3 4-3 5-1l2 3c1 1 0 2-1 3 1 3 3 5 6 7 1-1 2-2 3-1l3 2c2 1 1 3-1 5-6 3-20-10-17-18z"/>
        </svg>
        Tel - 403.555.0148 (VANT)<br>Fax- 403.555.0172
      </div>
      <div class="footer-item footer-address">
        <svg viewBox="0 0 32 32" fill="none" stroke="var(--brand-blue)" stroke-width="1.6">
          <path d="M14 28C7 20 4 15 4 11a10 10 0 0 1 19-4"/>
          <circle cx="14" cy="11" r="3.5"/>
          <path d="M17 20l7-6 7 6v9H17z"/>
          <rect x="22" y="23" width="4" height="6"/>
        </svg>
        The Marwick Block - 6127-48St.<br>Box 2716 Olds, AB<br>T2K 3M8
      </div>
      <div class="footer-item footer-web">
        <svg viewBox="0 0 32 32" fill="none" stroke="var(--brand-blue)" stroke-width="1.2">
          <circle cx="16" cy="14" r="12"/>
          <ellipse cx="16" cy="14" rx="5" ry="12"/>
          <path d="M4 14h24M6 8h20M6 20h20M16 26v3M3 29h26"/>
        </svg>
        www.vantagepsychology-example.ca
      </div>
    </footer>
  </section>

  <section class="sheet card-front" aria-label="Business card front">
    <div class="brand-mark"></div>
    <div class="brand-name">Vantage Psychology</div>
  </section>

  <section class="sheet card-back" aria-label="Business card back">
    <div class="card-back-panel" role="img" aria-label="Blue panel reserved for the brand symbol artwork"></div>
    <div class="card-back-info">
      <div class="brand-mark"></div>
      <div class="brand-name">Vantage Psychology</div>
      <ul class="contact-list">
        <li class="contact-row is-orange">
          <svg viewBox="0 0 16 16" fill="var(--brand-orange)"><circle cx="7" cy="5" r="3.5"/><path d="M1 15c0-5 3-6 6-6s6 1 6 6z"/></svg>
          Mr. xyz xyz
        </li>
        <li class="contact-row">
          <svg viewBox="0 0 16 16" fill="none" stroke="var(--brand-blue)" stroke-width="0.9"><rect x="1" y="1" width="14" height="14"/><path d="M3.5 4.5c1-1.5 2-1.5 2.5-.5l1 1.5c.5.5 0 1-.5 1.5.5 1.5 1.5 2.5 3 3.5.5-.5 1-1 1.5-.5l1.5 1c1 .5.5 1.5-.5 2.5-3 1.5-10-5-8.5-9z"/></svg>
          Tel - 403.555.0148 (VANT)
        </li>
        <li class="contact-row is-orange">
          <svg viewBox="0 0 16 16" fill="none" stroke="var(--brand-orange)" stroke-width="0.9"><rect x="1" y="6" width="4" height="9"/><rect x="5" y="7" width="10" height="8"/><rect x="7" y="2" width="6" height="5"/><path d="M8 10h5M8 12h5"/></svg>
          Fax- 403.555.0172
        </li>
        <li class="contact-row is-tall">
          <svg viewBox="0 0 16 16" fill="none" stroke="var(--brand-blue)" stroke-width="1"><path d="M7 15C3 10 2 8 2 6a5 5 0 0 1 9.5-2"/><circle cx="7" cy="6" r="1.8"/><path d="M9 10.5l3.5-3 3.5 3V15H9z"/></svg>
          The Marwick Block - 6127-48St.<br>Box 2716 Olds, AB<br>T2K 3M8
        </li>
        <li class="contact-row is-orange">
          <svg viewBox="0 0 16 16" fill="none" stroke="var(--brand-orange)" stroke-width="0.9"><circle cx="8" cy="7" r="6"/><ellipse cx="8" cy="7" rx="2.5" ry="6"/><path d="M2 7h12M8 13v2M2 15h12"/></svg>
          www.vantagepsychology-example.ca
        </li>
      </ul>
    </div>
  </section>

</main>
</body>
</html>
```